Automotive eCommerce Business looking for a business card design

Looking for a clean and simple business card design. Our company name is "Harbor Crest Auto" and we are a company specializing in the ecommerce sales of automotive parts, specifically for pick up trucks and large SUVs. Our company colours are red, black, and white.

Feel free to use the logo provided or create a new logo that you seem fit. Looking forward to your creative ideas!

Industry/Entity Type

Automotive

Contact Information for Business Card

We were thinking of a possibly two-sided design featuring just the logo and company name on one side, and personal information on the other side. Single sided designs will be considered as well.

Font styles to use
Serif
Sans Serif
Decorative

Colors
ec1f27
ffffff
000000

Requirements
Must have
• Space for employee's name, title, phone number and email address, along with the company address and website somewhere.

```html
<!DOCTYPE html>
<html lang="en">
<head>
<meta charset="utf-8">
<title>Harbor Crest Auto — Business Card</title>
<link href="https://fonts.googleapis.com/css2?family=Lato:wght@400;700&display=swap" rel="stylesheet">
<style>
  :root {
    --brand-red: #ec1f27;
    --card-slate: #30353f;
    --card-slate-light: #4a4f5a;
    --ink-white: #ffffff;
    --line-white: #e8e8e8;
    --stage-top: #e7e3de;
    --stage-bottom: #222222;
    --mark-grey: #5e5e5e;
  }
  html, body {
    margin: 0;
    padding: 0;
    width: 1200px;
    height: 1200px;
    overflow: hidden;
    font-family: "Lato", "Gill Sans", sans-serif;
  }
  .canvas {
    position: relative;
    width: 1200px;
    height: 1200px;
  }
  .card-stage {
    position: absolute;
    inset: 0 0 526px 0;
    background: var(--stage-top);
  }
  .mark-stage {
    position: absolute;
    top: 674px;
    left: 0;
    width: 1200px;
    height: 526px;
    background: radial-gradient(ellipse at 50% 40%, #2b2b2b 0%, var(--stage-bottom) 55%, #161616 100%);
  }
  .card {
    position: absolute;
    top: 236px;
    width: 378px;
    height: 216px;
    box-shadow: 0 6px 14px rgba(0,0,0,.35);
  }
  .card--front { left: 103px; }
  .card--back { left: 665px; }
  .card svg { display: block; }
  .wordmark {
    position: absolute;
    top: 936px;
    transform: translate(-50%, -50%);
    font-size: 22px;
    font-weight: 700;
    letter-spacing: .04em;
    white-space: nowrap;
  }
  .wordmark--mono { left: 358px; color: var(--mark-grey); }
  .wordmark--brand { left: 606px; color: var(--brand-red); }
  .wordmark--solid { left: 875px; color: var(--brand-red); }
  .svg-text { font-family: "Lato", "Gill Sans", sans-serif; }
</style>
</head>
<body>
<div class="canvas">
  <section class="card-stage">
    <!-- Front: personal details -->
    <div class="card card--front">
      <svg width="378" height="216" viewBox="0 0 378 216">
        <defs>
          <linearGradient id="slate-front" x1="1" y1="0" x2="0" y2="1">
            <stop offset="0" stop-color="var(--card-slate-light)"/>
            <stop offset="1" stop-color="var(--card-slate)"/>
          </linearGradient>
        </defs>
        <rect class="card-face" width="378" height="216" fill="url(#slate-front)"/>
        <line class="card-divider" x1="193" y1="0" x2="193" y2="216" stroke="#23272f" stroke-width="1"/>
        <polyline class="corner-line" points="0,31 37,26 70,1" fill="none" stroke="var(--line-white)" stroke-width="1"/>
        <polyline class="base-line" points="123,216 193,198 263,216" fill="none" stroke="var(--line-white)" stroke-width="1"/>
        <polygon class="base-accent" points="165,216 193,209 221,216" fill="var(--brand-red)"/>

        <text class="svg-text person-name" x="172" y="150" text-anchor="end" font-size="21" y-offset="0">
          <tspan fill="var(--brand-red)" transform="translate(0,0)" dy="-2">JOHN</tspan><tspan fill="var(--ink-white)">DOE</tspan>
        </text>
        <text class="svg-text person-role" x="172" y="165" text-anchor="end" font-size="8.5" fill="var(--line-white)">JOB POSITION</text>

        <g class="contact-list svg-text" font-size="6.2" fill="var(--ink-white)">
          <circle cx="209" cy="90" r="6" fill="var(--brand-red)"/>
          <rect x="205.5" y="87.5" width="7" height="5" fill="none" stroke="#fff" stroke-width=".8"/>
          <polyline points="205.5,87.5 209,90.5 212.5,87.5" fill="none" stroke="#fff" stroke-width=".8"/>
          <text x="230" y="92">JOHNDOE<tspan fill="var(--brand-red)">@</tspan>HARBORCRESTAUTO.COM</text>

          <circle cx="209" cy="109" r="6" fill="var(--brand-red)"/>
          <rect x="205.5" y="106.5" width="7" height="5" rx="1" fill="#fff"/>
          <text x="230" y="106"><tspan fill="var(--brand-red)">+44</tspan> 5550 2345 0111</text>
          <text x="230" y="115"><tspan fill="var(--brand-red)">+44</tspan> 5550 2221 0324</text>

          <circle cx="209" cy="131" r="6" fill="var(--brand-red)"/>
          <path d="M209 135 L206.4 130.5 A3 3 0 1 1 211.6 130.5 Z" fill="#fff"/>
          <text x="230" y="129">JOHN'S ADDRESS, CITY, COUNTY</text>
          <text x="230" y="138">BUSINESS ADDRESS, CITY, COUNTY</text>

          <circle cx="209" cy="150" r="6" fill="var(--brand-red)"/>
          <circle cx="209" cy="150" r="3.3" fill="none" stroke="#fff" stroke-width=".7"/>
          <line x1="205.7" y1="150" x2="212.3" y2="150" stroke="#fff" stroke-width=".6"/>
          <text x="230" y="152">WWW.<tspan fill="var(--brand-red)">HARBORCREST</tspan>AUTO.COM</text>
        </g>
      </svg>
    </div>

    <!-- Back: company name -->
    <div class="card card--back">
      <svg width="378" height="216" viewBox="0 0 378 216">
        <defs>
          <linearGradient id="slate-back" x1="1" y1="0" x2="0" y2="1">
            <stop offset="0" stop-color="var(--card-slate-light)"/>
            <stop offset="1" stop-color="var(--card-slate)"/>
          </linearGradient>
          <linearGradient id="red-blade" x1="0" y1="0" x2="0" y2="1">
            <stop offset="0" stop-color="#f4484d"/>
            <stop offset="1" stop-color="#d7080f"/>
          </linearGradient>
        </defs>
        <rect class="card-face" width="378" height="216" fill="url(#slate-back)"/>
        <polygon class="white-blade" points="4,2 94,216 23,216 62,180" fill="#d9d9d9"/>
        <polygon class="red-blade" points="1,1 62,180 23,216 0,216" fill="url(#red-blade)"/>
        <text class="svg-text company-name" x="192" y="154" text-anchor="middle" font-size="11.5" fill="var(--ink-white)" letter-spacing=".3">HARBOR CREST AUTO LTD.</text>
      </svg>
    </div>
  </section>

  <section class="mark-stage" aria-label="Name variations">
  </section>
  <div class="wordmark wordmark--mono">Harbor Crest Auto</div>
  <div class="wordmark wordmark--brand">Harbor Crest Auto</div>
  <div class="wordmark wordmark--solid">Harbor Crest Auto</div>
</div>
</body>
</html>
```